we do all sorts of cleaning however bookings are limited!
why not chose the right cleaners for you!
pressure cleaning, window cleaning, office, end of lease clean, accommodation, industrial and commercial cleaning and house cleaning

Logo Text

Bright Nest Cleaning Service

```html
<!DOCTYPE html>
<html lang="en">
<head>
<meta charset="utf-8">
<title>Bright Nest Cleaning Service – Business Card</title>
<link rel="stylesheet" href="https://fonts.googleapis.com/css2?family=Open+Sans:wght@400;600;800&family=Montserrat:wght@800&family=Great+Vibes&display=swap">
<style>
  :root {
    --stage: #2a2b2e;
    --card: #1b1b1d;
    --card-edge: #242427;
    --blue: #1ab0ef;
    --blue-deep: #0b6fa8;
    --green: #8cd43a;
    --text: #f2f2f2;
    --muted: #c9c9cc;
    --ornament: #3a3a3e;
    --ornament-light: #5c5c61;
  }
  * { box-sizing: border-box; margin: 0; padding: 0; }
  html, body { width: 1200px; height: 840px; overflow: hidden; }
  body {
    background: var(--stage);
    font-family: "Open Sans", Arial, sans-serif;
    color: var(--text);
    position: relative;
  }
  .card {
    position: absolute;
    width: 580px;
    height: 330px;
    background: var(--card);
    border-radius: 26px;
    box-shadow: 0 18px 40px rgba(0,0,0,.45);
    overflow: hidden;
  }
  .card--services { left: 50px; top: 60px; }
  .card--contact { left: 570px; top: 450px; }

  /* brand lockup */
  .brand { display: flex; align-items: center; gap: 10px; }
  .brand__dot { width: 16px; height: 16px; border-radius: 50%; background: var(--green); flex: none; }
  .brand__name {
    color: var(--blue);
    font-weight: 800;
    line-height: 1;
  }
  .brand__name span { display: block; }
  .brand__name .brand__line1 { font-size: 40px; letter-spacing: -.5px; }
  .brand__name .brand__line2 { font-size: 15px; letter-spacing: 2.2px; margin-top: 4px; }

  /* services card */
  .card--services .brand { position: absolute; left: 0; right: 0; top: 34px; justify-content: center; }
  .ornament { position: absolute; }
  .ornament--splash { left: 22px; top: 92px; width: 90px; height: 150px; }
  .ornament--leaf { right: 18px; top: 20px; width: 110px; height: 160px; }
  .pitch {
    position: absolute; left: 0; right: 0; top: 128px;
    text-align: center; font-size: 15px; line-height: 1.35; color: var(--text);
  }
  .band {
    position: absolute; left: 80px; right: 60px; top: 183px; height: 34px;
    background: linear-gradient(90deg, rgba(11,111,168,0) 0%, var(--blue-deep) 22%, var(--blue) 60%);
    display: flex; align-items: center; justify-content: center;
  }
  .band__text {
    font-family: "Montserrat", Arial, sans-serif;
    font-weight: 800; font-size: 16px; color: #ffffff;
  }
  .services {
    position: absolute; left: 0; right: 0; top: 232px;
    list-style: none; text-align: center;
    font-size: 14.5px; line-height: 1.6; color: var(--text);
  }
  .services li span { white-space: nowrap; }
  .services .dot {
    display: inline-block; width: 8px; height: 8px; border-radius: 50%;
    background: var(--green); margin: 0 6px 1px 8px; vertical-align: middle;
  }

  /* contact card */
  .card--contact .brand { position: absolute; right: 42px; top: 40px; }
  .rule { position: absolute; height: 1px; background: var(--text); }
  .rule--top { left: 250px; right: 40px; top: 126px; }
  .rule--mid { left: 36px; width: 250px; top: 210px; }
  .person { position: absolute; left: 38px; top: 130px; }
  .person__name {
    font-family: "Great Vibes", cursive;
    font-size: 46px; line-height: 1;
  }
  .person__first { color: var(--blue); }
  .person__last { color: var(--green); }
  .person__role { font-size: 16px; margin-top: 4px; color: var(--text); }
  .contacts { position: absolute; left: 40px; top: 222px; list-style: none; font-size: 15px; line-height: 1.7; }
  .contacts li { display: flex; align-items: center; gap: 8px; }
  .contacts svg { width: 15px; height: 15px; flex: none; }
  .address {
    position: absolute; right: 40px; top: 150px; text-align: right;
    font-size: 16px; line-height: 1.35; color: var(--text);
  }
</style>
</head>
<body>

<section class="card card--services" aria-label="Business card, services side">
  <div class="ornament ornament--splash" role="img" aria-label="Decorative water splash in dark grey">
    <svg viewBox="0 0 90 150" width="90" height="150"><ellipse cx="45" cy="75" rx="40" ry="70" fill="var(--ornament)"/></svg>
  </div>
  <div class="ornament ornament--leaf" role="img" aria-label="Decorative leaf in dark grey">
    <svg viewBox="0 0 110 160" width="110" height="160"><ellipse cx="55" cy="80" rx="50" ry="76" fill="var(--ornament)"/></svg>
  </div>

  <div class="brand">
    <span class="brand__dot"></span>
    <p class="brand__name"><span class="brand__line1">Bright Nest</span><span class="brand__line2">CLEANING SERVICE</span></p>
  </div>

  <p class="pitch">we do all sorts of cleaning<br>however bookings are limited!</p>

  <div class="band"><p class="band__text">why not chose the right cleaners for you!</p></div>

  <ul class="services">
    <li><span class="dot"></span>Pressure Cleaning<span class="dot"></span>Window Cleaning<span class="dot"></span>Office</li>
    <li><span class="dot"></span>End Of Lease Clean<span class="dot"></span>Accommodation</li>
    <li><span class="dot"></span>Industrial And Commercial Cleaning<span class="dot"></span>House Cleaning</li>
  </ul>
</section>

<section class="card card--contact" aria-label="Business card, contact side">
  <div class="brand">
    <span class="brand__dot"></span>
    <p class="brand__name"><span class="brand__line1">Bright Nest</span><span class="brand__line2">CLEANING SERVICE</span></p>
  </div>
  <div class="rule rule--top"></div>

  <div class="person">
    <p class="person__name"><span class="person__first">Daniel</span> <span class="person__last">Porter</span></p>
    <p class="person__role">Managing Director</p>
  </div>
  <div class="rule rule--mid"></div>

  <ul class="contacts">
    <li>
      <svg viewBox="0 0 16 16" aria-hidden="true"><path fill="var(--blue)" d="M3.6 1.2l2.3 2.6-1.3 1.8c.9 2 2.6 3.7 4.6 4.6l1.8-1.3 2.6 2.3-1.4 2.4C6.7 15.3.7 9.3.9 2.6z"/></svg>
      <span>044-555 210 347</span>
    </li>
    <li>
      <svg viewBox="0 0 16 16" aria-hidden="true"><rect x="1" y="3" width="14" height="10" rx="1.5" fill="var(--blue)"/><path d="M1.5 4l6.5 5 6.5-5" fill="none" stroke="var(--card)" stroke-width="1.4"/></svg>
      <span>info@brightnestclean.com</span>
    </li>
    <li>
      <svg viewBox="0 0 16 16" aria-hidden="true"><circle cx="8" cy="8" r="7" fill="var(--blue)"/><g fill="none" stroke="var(--card)" stroke-width="1"><ellipse cx="8" cy="8" rx="3" ry="7"/><path d="M1 8h14M2.5 4.5h11M2.5 11.5h11"/></g></svg>
      <span>www.brightnestclean.com</span>
    </li>
  </ul>

  <p class="address">18 Harbour Lane, Easton<br>State, Zip 4021</p>
</section>

</body>
</html>
```